Sponsorship and registration document for Charity Golf Day 2022

The project requires 2 documents to be updated to look more graphically savvy and professionally presentable.
1. Charity golf day sponsorship document
2. One page registration document.
The text has been completed. Text not to be changed - just graphics.
New images would be preferred.
The logos have been provided.

Target Market(s)

Corporate Sponsors and Golf players

Requirements
Must have
• Golf Theme

```html
<!DOCTYPE html>
<html lang="en">
<head>
<meta charset="utf-8">
<title>Charity Golf Day 2022 – Sponsorship Proposal</title>
<link rel="stylesheet" href="https://fonts.googleapis.com/css2?family=Roboto:wght@300;400;500;700&family=Roboto+Condensed:wght@400;700&display=swap">
<style>
:root{
  --navy:#34405b;
  --navy-deep:#2a3449;
  --orange:#f19d33;
  --ink:#4a4f5c;
  --band:#e4e5e8;
  --bg:#d6d7d9;
  --white:#ffffff;
  --gold-a:#f6d27a;--gold-b:#b8842a;
  --silver-a:#f2f2f2;--silver-b:#9a9da2;
  --bronze-a:#e6a57a;--bronze-b:#8f4f2b;
}
*{box-sizing:border-box;margin:0;padding:0}
html,body{width:1200px;height:3145px;overflow:hidden}
body{background:var(--bg);font-family:"Roboto",Arial,sans-serif;color:var(--ink)}
.stage{position:absolute;left:0;top:0;width:983px;height:2576px;transform:scale(1.22075);transform-origin:0 0}
.spread{position:absolute;left:100px;width:792px;height:560px;background:var(--white);overflow:hidden;box-shadow:0 3px 8px rgba(0,0,0,.22)}
.spread::after{content:"";position:absolute;left:395px;top:0;width:2px;height:100%;background:linear-gradient(90deg,rgba(0,0,0,.05),rgba(0,0,0,0))}
.abs{position:absolute}
svg.abs{display:block}
p,li{line-height:1.35}
ul{list-style:none}
.dots li{position:relative;padding-left:7px}
.dots li::before{content:"•";position:absolute;left:0}

/* brand lockup */
.lockup{display:flex;align-items:center;gap:5px;color:var(--navy);font-weight:400}
.lockup .mark{width:22px;height:22px;border-radius:50%;background:var(--orange);flex:none}
.lockup .name{font-size:15px;line-height:1.05}

/* cover */
.cover-title{left:396px;width:396px;text-align:center;color:var(--orange);font-family:"Roboto Condensed",sans-serif;font-weight:700;font-size:39px;top:24px;letter-spacing:.3px}
.cover-date{left:396px;width:396px;text-align:center;color:var(--white);font-family:"Roboto Condensed",sans-serif;font-weight:700;font-size:14px;line-height:15px;top:66px}
.contact{left:27px;top:397px;color:var(--navy);font-size:7px;line-height:9.8px}
.contact h4{font-size:10px;font-weight:700;line-height:12px}
.contact .lead{font-size:9.5px;font-weight:700;line-height:12px}
.footer-strip{top:535px;left:0;width:396px;height:25px;background:var(--orange);color:var(--white);font-size:7px;display:flex;align-items:center;gap:0}
.footer-strip span{position:absolute;display:flex;align-items:center;gap:4px}
.proposal-band{left:438px;top:426px}
.proposal-title{left:440px;width:322px;top:429px;text-align:center;color:var(--white);font-size:20px;font-weight:400;letter-spacing:.4px}
.proposal-sub{left:396px;width:396px;top:461px;text-align:center;color:var(--orange);font-weight:700;font-size:12.5px}
.proposal-copy{left:396px;width:396px;top:483px;text-align:center;color:var(--navy);font-size:11.5px;line-height:15px}
.cover-web{left:620px;top:539px;color:var(--white);font-size:11px;display:flex;align-items:center;gap:5px}

/* inner pages */
.lede{left:17px;top:172px;width:350px;color:var(--navy);font-size:13.5px;line-height:14.6px;font-weight:400}
.rule{left:17px;top:221px;width:128px;height:2px;background:var(--navy)}
.body{font-size:7px;line-height:9.4px;color:var(--ink)}
.label{color:var(--navy);font-weight:700;font-size:8.5px}
.format-row{left:17px;display:flex;align-items:center;gap:9px;font-size:8.5px;color:var(--navy)}
.format-row .icon{width:14px;height:14px;background:var(--orange);border-radius:2px;display:flex;align-items:center;justify-content:center}
.sign-off{left:17px;top:490px;color:var(--navy);font-size:7.5px;line-height:9px}
.sign-off small{display:block;font-size:5.5px;line-height:7px;color:var(--ink)}
.signature{left:182px;top:507px;width:80px;height:18px;background:#eceef3;border-radius:3px}
.why-title{left:419px;top:22px;color:var(--orange);font-size:11px;font-weight:500}
.why-list{left:419px;top:56px;width:245px;color:var(--white);font-size:6.4px}
.why-list li{line-height:8px;margin-bottom:4.6px}
.ask-title{left:419px;top:175px;color:var(--navy);font-size:12px}
.ask-list{left:419px;top:201px;color:var(--ink);font-size:7px}
.ask-list li{line-height:12.6px}
.achieve{left:419px;top:280px;width:351px;height:98px;background:var(--navy);border-radius:4px}
.achieve h3{position:absolute;top:8px;width:100%;text-align:center;color:var(--orange);font-size:10.5px;font-weight:500}
.achieve ul{position:absolute;left:10px;top:29px;width:335px}
.achieve li{position:relative;padding-left:14px;color:var(--white);font-size:6.4px;line-height:7.2px;margin-bottom:6px}
.achieve li::before{content:"";position:absolute;left:0;top:2px;width:6px;height:6px;border-radius:50%;background:var(--orange)}
.achieve b{color:var(--orange);font-size:10px;font-weight:400}

/* course page */
.date-tag-text{left:20px;top:30px;color:var(--white);line-height:1}
.date-tag-text strong{display:block;font-size:13px;font-weight:500;line-height:15px}
.date-tag-text span{display:block;font-size:7px;line-height:9px}
.course-copy{left:17px;top:80px;width:360px;color:var(--white);font-size:9px;line-height:12px}
.small-head{color:var(--navy);font-size:8px;font-weight:700}
.plain-list{font-size:7px;color:var(--ink)}
.plain-list li{line-height:10px}
.expect-list li{line-height:13px;font-size:7px}
.schedule{left:20px;top:388px;width:348px;height:98px;background:var(--orange);border-radius:6px;overflow:hidden}
.schedule .row{position:absolute;left:0;width:100%;height:12px;color:var(--white);font-size:8.5px;line-height:12px}
.schedule .row:nth-child(odd){background:rgba(255,255,255,.12)}
.schedule .t{position:absolute;left:28px}
.schedule .e{position:absolute;left:147px}
.schedule-tab{left:48px;top:381px;width:100px;height:20px;background:var(--navy);color:var(--white);font-size:10px;font-weight:700;text-align:center;line-height:20px;border-radius:2px}
.extra-note{left:20px;top:500px;width:270px;font-size:7px;line-height:12px;color:var(--navy)}
.opps-title{left:396px;width:396px;top:20px;text-align:center;color:var(--white);font-size:12.5px;font-weight:700;letter-spacing:.3px}
.tier-badge{width:46px;height:46px;border-radius:50%;display:flex;flex-direction:column;align-items:center;justify-content:center;font-family:"Roboto Condensed",sans-serif;font-size:9px;line-height:10px;font-weight:700;box-shadow:0 1px 3px rgba(0,0,0,.35)}
.tier-bar{height:14px;width:210px;color:var(--white);font-size:6.5px;line-height:14px;padding-left:5px}
.tier-list{left:472px;width:308px;font-size:6.1px;color:var(--ink)}
.tier-list li{line-height:7.6px}

/* forms */
.form-head{color:var(--orange);font-size:11.5px;font-weight:700}
.form-text{font-size:7px;line-height:9.5px;color:var(--navy)}
.form-text b{font-weight:700}
.box{display:inline-block;width:8px;height:8px;border:1px solid var(--navy);vertical-align:-1px;margin:0 4px}
.field-row{left:17px;width:345px;height:15px;font-size:7px;line-height:15px;padding-left:5px;color:var(--navy)}
.field-row.shade{background:var(--band)}
.player{left:419px;width:345px}
.player .bar{height:14px;background:var(--band);font-size:7px;line-height:14px;padding-left:5px;color:var(--navy);font-weight:500}
.player .cap{height:14px;font-size:7px;line-height:16px;padding-left:5px;color:var(--navy);border-bottom:1px solid var(--band)}
.fine{font-size:5.6px;line-height:7px;color:var(--navy)}
</style>
</head>
<body>
<main class="stage">

<!-- Spread 1: cover -->
<section class="spread" style="top:72px" aria-label="Front and back cover">
  <div class="abs" style="left:0;top:0;width:792px;height:375px;background:var(--navy)"></div>
  <svg class="abs" style="left:0;top:0" width="792" height="375" viewBox="0 0 792 375" role="img" aria-label="Golfer in a lime shirt finishing a swing on a fairway with hills and trees behind">
    <defs>
      <linearGradient id="coverScene" x1="0" y1="0" x2="0" y2="1">
        <stop offset="0" stop-color="#a9bccb"/>
        <stop offset=".35" stop-color="#8aa3a8"/>
        <stop offset=".6" stop-color="#4e7a3a"/>
        <stop offset="1" stop-color="#6f9a48"/>
      </linearGradient>
      <linearGradient id="coverFade" x1="0" y1="0" x2="1" y2="0">
        <stop offset=".2" stop-color="#34405b" stop-opacity=".95"/>
        <stop offset=".55" stop-color="#34405b" stop-opacity="0"/>
      </linearGradient>
    </defs>
    <polygon points="242,102 792,102 792,375 182,375" fill="url(#coverScene)"/>
    <polygon points="242,102 792,102 792,375 182,375" fill="url(#coverFade)"/>
    <polygon points="229,102 242,102 182,375 169,375" fill="#f19d33"/>
  </svg>
  <h1 class="abs cover-title">CHARITY GOLF DAY</h1>
  <p class="abs cover-date">FRIDAY 25 MARCH 2022<br>Elmridge Golf Club</p>

  <div class="abs contact">
    <h4>CONTACT</h4>
    <div class="lead">Helena (Marsh) Whitford</div>
    Convenor<br>
    Co - President, Lakeside Service Club<br>
    Mobile: 0400 555 018<br>
    Email: helena.whitford@mailbox.com<br>
    Web: www.lsc.org.au/golf-day<br><br>
    Clara Benedetti<br>
    Event Manager<br>
    Email: clara.benedetti@netmail.com
  </div>
  <div class="abs lockup" style="left:240px;top:474px">
    <div class="name" style="text-align:right">Lakeside<br>Service Club</div>
    <div class="mark" style="width:30px;height:30px"></div>
  </div>
  <div class="abs footer-strip">
    <span style="left:27px"><svg width="7" height="7" viewBox="0 0 10 10"><circle cx="5" cy="5" r="4.2" fill="none" stroke="#fff" stroke-width="1"/><path d="M1 5h8M5 .8c-2 2.5-2 5.9 0 8.4M5 .8c2 2.5 2 5.9 0 8.4" fill="none" stroke="#fff" stroke-width=".8"/></svg>www.lsc.org.au/golf-day</span>
    <span style="left:173px"><svg width="7" height="7" viewBox="0 0 10 10"><path d="M2 1l2 2-1 1.5c.6 1.2 1.4 2 2.5 2.5L7 6l2 2-1.5 1.5C4 9 1 6 .5 2.5z" fill="#fff"/></svg>0400 555 018</span>
    <span style="left:267px"><svg width="7" height="6" viewBox="0 0 10 8"><rect x=".5" y=".5" width="9" height="7" fill="#fff"/><path d="M.5.5L5 4.5 9.5.5" fill="none" stroke="#f19d33" stroke-width=".9"/></svg>helena.whitford@mailbox.com</span>
  </div>

  <div class="abs lockup" style="left:545px;top:385px">
    <div class="name" style="text-align:center">Lakeside<br>Service Club</div>
    <div class="mark"></div>
  </div>
  <svg class="abs proposal-band" width="326" height="27" viewBox="0 0 326 27" aria-hidden="true">
    <polygon points="10,0 326,0 316,27 0,27" fill="#f19d33"/>
    <polygon points="16,0 316,0 306,27 6,27" fill="#34405b"/>
  </svg>
  <h2 class="abs proposal-title">SPONSORSHIP PROPOSAL</h2>
  <p class="abs proposal-sub">SUPPORTING PROSTATE CANCER RESEARCH</p>
  <p class="abs proposal-copy">Help us hit prostate cancer off the green<br>and beat the most common cancer in Australian men.</p>
  <svg class="abs" style="left:396px;top:530px" width="396" height="30" viewBox="0 0 396 30" aria-hidden="true">
    <rect x="0" y="5" width="396" height="25" fill="#f19d33"/>
    <polygon points="182,0 396,0 396,30 172,30" fill="#34405b"/>
  </svg>
  <div class="abs cover-web"><svg width="10" height="10" viewBox="0 0 10 10"><circle cx="5" cy="5" r="4.2" fill="none" stroke="#fff" stroke-width=".9"/><path d="M1 5h8M5 .8c-2 2.5-2 5.9 0 8.4M5 .8c2 2.5 2 5.9 0 8.4" fill="none" stroke="#fff" stroke-width=".8"/></svg>www.lsc.org.au/golf-day</div>
</section>

<!-- Spread 2: introduction -->
<section class="spread" style="top:712px" aria-label="Introduction and why prostate cancer">
  <div class="abs" style="left:0;top:0;width:396px;height:155px;background:linear-gradient(180deg,#4f6a3a 0%,#6d8f4a 45%,#9cc05c 75%,#7aa445 100%)" role="img" aria-label="Putting green with a sand bunker framed by gum trees"></div>
  <h2 class="abs lede">Join us for an exclusive day on the private Elmridge Golf Course, with all proceeds going to support Prostate Cancer Research, Awareness and Support.</h2>
  <div class="abs rule"></div>
  <p class="abs body" style="left:17px;top:236px;width:358px">The Lakeside Service Club will again be holding its Charity Golf Day with all proceeds used to support the Prostate Cancer Research, awareness and Support Programs. The venue will be the prestigious Elmridge Golf Club on Friday 25 March 2022, with a shotgun start at 8:00 am.</p>
  <p class="abs body" style="left:17px;top:272px;width:358px">We have enclosed for your information a copy of our promotional sponsor packages that outline the event, sponsorship package options and inclusions.</p>
  <div class="abs label" style="left:17px;top:305px">THE FORMAT OF THE DAY INVOLVES:</div>
  <div class="abs format-row" style="top:324px"><span class="icon"><svg width="8" height="8" viewBox="0 0 10 10"><rect x="2" y="1" width="6" height="8" fill="none" stroke="#fff"/><path d="M3.5 4h3M3.5 6h3" stroke="#fff"/></svg></span>Player registration, refreshments and light breakfast from 7:00am</div>
  <div class="abs format-row" style="top:344px"><span class="icon"><svg width="8" height="8" viewBox="0 0 10 10"><path d="M3 9V1l5 2-5 2" fill="none" stroke="#fff"/></svg></span>Ambrose competition starting at 8:00am</div>
  <div class="abs format-row" style="top:364px"><span class="icon"><svg width="8" height="8" viewBox="0 0 10 10"><path d="M2 1h6v3a3 3 0 0 1-6 0zM5 7v2M3 9h4" fill="none" stroke="#fff"/></svg></span>Two Course lunch and presentations in the club house from 12:30pm</div>
  <p class="abs body" style="left:17px;top:396px;width:358px">Your commitment to supporting health programs in our community is truly appreciated. With assistance from sponsors such as yourself, we will continue to see improvements in the support and treatment for men and their families with prostate cancer.</p>
  <p class="abs body" style="left:17px;top:434px;width:358px">We hope that you will consider supporting the worthwhile event that is open to any organisation or individual who wishes to enjoy the benefits of playing golf at the prestigious Elmridge Golf Club. For more information, please check the website <b style="color:var(--navy)">www.lsc.org.au/golf-day</b> or should you wish to discuss any aspect of the event, please contact me on <b style="color:var(--navy)">0400 555 018</b>.</p>
  <div class="abs sign-off">Yours sincerely,<br><b>Helena (Marsh) Whitford Convener</b>
    <small style="margin-top:3px">Co - President 2021 -2022<br>Secretary 2021 - 2022<br>Lakeside Service Club</small></div>
  <div class="abs signature" role="img" aria-label="Handwritten signature of the convener"></div>

  <div class="abs" style="left:396px;top:0;width:396px;height:162px;background:linear-gradient(160deg,#5c8a3a 0%,#9bc456 60%,#c7df7e 100%)" role="img" aria-label="Golf ball beside an iron club head on the grass"></div>
  <svg class="abs" style="left:396px;top:0" width="396" height="162" viewBox="0 0 396 162" aria-hidden="true">
    <polygon points="0,0 232,0 245,15 0,15" fill="#f19d33"/>
    <polygon points="0,15 245,15 368,155 0,155" fill="#34405b"/>
    <rect x="0" y="155" width="396" height="7" fill="#f19d33"/>
  </svg>
  <h3 class="abs why-title">WHY PROSTATE CANCER?</h3>
  <ul class="abs dots why-list">
    <li>Prostate cancer is the most diagnosed cancer in Australian men.</li>
    <li>Approximately 20,000 Australian men are diagnosed with prostate cancer each year.</li>
    <li>Over 200,000 Australian men are living with a diagnosis prostate cancer.</li>
    <li>95% of Australian men diagnosed with prostate cancer survive for at least 5 years.</li>
    <li>Almost 3,500 Australian men die of prostate cancer each year.</li>
  </ul>
  <h3 class="abs ask-title">Why are we asking you to be involved?</h3>
  <ul class="abs dots ask-list">
    <li>Every day 54 Australian men will be told they have prostate cancer</li>
    <li>70% of research applications are unfunded</li>
    <li>1 in 6 men will suffer from prostate cancer</li>
    <li>9 families lose a loved one to prostate cancer every day</li>
    <li>Only 1 in 3 men have access to a specialist nurse</li>
  </ul>
  <div class="abs achieve">
    <h3>WHAT THIS FUNDRAISING EVENT CAN ACHIEVE</h3>
    <ul>
      <li><b>$12,500</b> – could provide funding for a researcher working for one month on a project to reduce side – effects post treatment.</li>
      <li><b>$30,000</b> – could provide funding for a senior scientist for three months working on a project to improve treatments for prostate cancer that has spread to the bones.</li>
      <li><b>$50,000</b> – could fund a project to improve early – diagnosis for men with a family history of prostate cancer</li>
    </ul>
  </div>
  <p class="abs body" style="left:419px;top:399px;width:355px">Proceeds from this event will be donated to Prostate Cancer Research Group at the Life Sciences Research Centre, Southgate University, to fund world leading, innovative research and to support men and their families affected by prostate cancer.</p>
  <p class="abs body" style="left:419px;top:437px;width:355px">Their innovative research program has a strong translational approach, involving lab-based studies with tissues donated by patients with prostate cancer. Their collaborative studies with clinicians and patient advocates address questions that are relevant to patient care. The findings have the potential to improve the management and outcomes of men with different stages of prostate cancer. Recent studies have informed international guidelines for diagnosis of prostate cancer and led to new clinical trials.</p>
  <p class="abs body" style="left:419px;top:505px;width:355px">For more information visit their website:<br><b style="color:var(--navy)">www.southgate.edu/life-sciences-centre/prostate-research</b></p>
  <div class="abs" style="left:0;top:551px;width:792px;height:9px;background:var(--navy)"></div>
</section>

<!-- Spread 3: the day and sponsorship tiers -->
<section class="spread" style="top:1332px" aria-label="Event details and sponsorship opportunities">
  <div class="abs" style="left:0;top:0;width:396px;height:147px;background:var(--navy)"></div>
  <svg class="abs" style="left:0;top:26px" width="196" height="34" viewBox="0 0 196 34" aria-hidden="true"><polygon points="0,0 196,0 184,34 0,34" fill="#f19d33"/></svg>
  <div class="abs date-tag-text"><strong>FRIDAY 25 MARCH 2022</strong><span>AT ELMRIDGE GOLF CLUB</span></div>
  <p class="abs course-copy">The Championship Par 72 layout of 6179 metres is a genuine test to all standards of players. Situated only 15 minutes from the city, the course meanders along the Elm River providing a beautiful vista and is home for 100's of species of native birds and tall-established trees.</p>

  <div class="abs small-head" style="left:17px;top:177px">BREAKFAST:</div>
  <ul class="abs dots plain-list" style="left:17px;top:191px"><li>Light Breakfast</li><li>Tea and coffee</li></ul>
  <div class="abs small-head" style="left:141px;top:177px">LUNCH:</div>
  <ul class="abs dots plain-list" style="left:141px;top:188px"><li>Two-Course Lunch</li><li>Drinks at Bar Prices</li></ul>
  <div class="abs small-head" style="left:17px;top:234px">WHAT ELSE TO EXPECT:</div>
  <ul class="abs dots expect-list" style="left:17px;top:246px;width:365px">
    <li>4-person Ambrose</li>
    <li>On course competitions such as nearest the pins and longest drive</li>
    <li>Trophies &amp; Prizes</li>
    <li>On the day you will have access to practice putting, chipping greens, and driving range</li>
    <li>A refreshment cart will circulate the golf course for players to purchase refreshments at own cost</li>
    <li>Hire Equipment</li>
    <li>Hire sets (Standard) $35.00 per set; (Premium) $50.00 per set</li>
    <li>Hire shoes $10.00 per pair</li>
    <li>Carts $40.00 each (Booking essential as numbers are limited, but it is an easy course to walk)</li>
  </ul>
  <div class="abs schedule">
    <div class="row" style="top:18px"><span class="t">7:00am to 7:30am:</span><span class="e">Registration</span></div>
    <div class="row" style="top:30px"><span class="t">7:15am:</span><span class="e">Breakfast</span></div>
    <div class="row" style="top:42px"><span class="t">7:45am:</span><span class="e">Player Briefing</span></div>
    <div class="row" style="top:54px"><span class="t">8:00am:</span><span class="e">Shotgun start</span></div>
    <div class="row" style="top:66px"><span class="t">12.30pm:</span><span class="e">Lunch, Presentation/Prizes</span></div>
    <div class="row" style="top:78px"><span class="t">3.00pm:</span><span class="e">Finish</span></div>
  </div>
  <div class="abs schedule-tab">SCHEDULE:</div>
  <p class="abs extra-note"><b>ADDITIONAL PLAYERS - $150 PER PERSON</b> - includes all green fees, light breakfast &amp; two (2) course lunch</p>

  <div class="abs" style="left:396px;top:0;width:396px;height:147px;background:linear-gradient(180deg,#8a7a3a 0%,#c9a44a 30%,#6f8a36 65%,#4f7a2c 100%)" role="img" aria-label="Golf ball on an orange tee beside a driver head on sunlit grass"></div>
  <svg class="abs" style="left:396px;top:0" width="40" height="147" viewBox="0 0 40 147" aria-hidden="true"><polygon points="0,0 30,0 0,147" fill="#34405b"/></svg>
  <h3 class="abs opps-title">SPONSORSHIP OPPORTUNITIES</h3>

  <div class="abs tier-badge" style="left:417px;top:165px;background:radial-gradient(circle at 40% 35%,var(--gold-a),var(--gold-b));color:#5a3d0c">GOLD<span>$5,000</span></div>
  <div class="abs tier-bar" style="left:465px;top:171px;background:linear-gradient(90deg,#b8842a,#e8b95a 80%,rgba(232,185,90,0))">The Gold Sponsor is entitled to the following:</div>
  <ul class="abs dots tier-list" style="top:191px">
    <li>Event naming rights</li>
    <li>Eight (8) representatives playing in the event, including all green fees, four (4) carts, light breakfast &amp; 2 course lunch</li>
    <li>Your company signage / banners displayed exclusively at club entrance and social area.</li>
    <li>Your logo and your company information on all promotional and marketing material being used on the day including our website, email to database and our social media channels.</li>
    <li>A Banner with company logo on the first hole</li>
    <li>Opportunity to say a few words at the beginning of the game as the chief sponsor of the event.</li>
    <li>Your company merchandise on display.</li>
    <li>Presenting the winners awards</li>
    <li>Free advertising in our Lakeside Service Club Newsletter, website, and social media channels for 12 months.</li>
    <li>Opportunity to "capture" prospective clients on the day</li>
    <li>Great Publicity: Be seen as being associated with an excellent cause</li>
  </ul>

  <div class="abs tier-badge" style="left:417px;top:315px;background:radial-gradient(circle at 40% 35%,var(--silver-a),var(--silver-b));color:#3f4247">SILVER<span>$2,500</span></div>
  <div class="abs tier-bar" style="left:465px;top:321px;background:linear-gradient(90deg,#8e9197,#c9cbcf 80%,rgba(201,203,207,0))">The Silver Sponsor is entitled to the following:</div>
  <ul class="abs dots tier-list" style="top:340px">
    <li>Four (4) representatives playing in the event, including all green fees, two (2) carts, light breakfast &amp; 2 course lunch</li>
    <li>Exclusive banner with your company logo on a tee of choice (except hole 1)</li>
    <li>Opportunity to say a few words as a major sponsor</li>
    <li>Your company merchandise on display</li>
    <li>Your logo and your company information on all promotional and marketing material being used on the day including our website, email to database and our social media channels.</li>
    <li>Free advertising in our Lakeside Service Club Newsletter, website and social media channels for 6 months.</li>
    <li>Opportunity to "capture" prospective clients on the day</li>
    <li>Great Publicity: Be seen as being associated with an excellent cause</li>
  </ul>

  <div class="abs tier-badge" style="left:417px;top:437px;background:radial-gradient(circle at 40% 35%,var(--bronze-a),var(--bronze-b));color:#3e1f0c">BRONZE<span>$650</span></div>
  <div class="abs tier-bar" style="left:465px;top:444px;background:linear-gradient(90deg,#9a5a34,#d8956a 80%,rgba(216,149,106,0))">This Bronze Sponsor is entitled to the following:</div>
  <ul class="abs dots tier-list" style="top:463px">
    <li>Two (2) representatives playing in the event, including all green fees, light breakfast &amp; 2 course lunch</li>
    <li>Exclusive banner with your company logo on a tee</li>
    <li>Your logo and your company information on all promotional and marketing material being used on the day including our website, email to database and our social media channels.</li>
    <li>Great Publicity: Be seen as being associated with an excellent cause</li>
    <li>Opportunity to "capture" prospective clients on the day</li>
    <li>Company merchandising display</li>
    <li>Additional players - $150 per person (including all green fees, light breakfast &amp; 2-course lunch).</li>
  </ul>
  <svg class="abs" style="left:0;top:548px" width="792" height="12" viewBox="0 0 792 12" aria-hidden="true"><polygon points="200,0 606,0 620,12 186,12" fill="#34405b"/></svg>
</section>

<!-- Spread 4: registration form -->
<section class="spread" style="top:1943px" aria-label="Payment and team registration form">
  <h3 class="abs form-head" style="left:17px;top:49px">PAYMENT OPTIONS:</h3>
  <div class="abs form-text" style="left:17px;top:72px"><b>BY CHEQUE:</b></div>
  <div class="abs form-text" style="left:65px;top:72px">Please make cheques payable to The Lakeside Service Club<br>PO Box 180<br>Lakeside East, Vic 3199</div>
  <div class="abs form-text" style="left:17px;top:122px"><b>BY DIRECT<br>DEPOSIT:</b></div>
  <div class="abs form-text" style="left:65px;top:122px">Account Name: Lakeside Service Club<br><b>BANK:</b> Harbour Community Bank<br>BSB: 611 200<br>Account Number: 482 316 590<br>Comment: LSCGolfDay/your name</div>
  <div class="abs form-text" style="left:17px;top:194px"><b>BY CREDIT<br>CARD:</b></div>
  <div class="abs form-text" style="left:65px;top:203px">CardOne<span class="box"></span><span style="margin-left:30px">PayLink</span><span class="box"></span></div>
  <div class="abs form-text" style="left:17px;top:224px">Card No. ____ ____ ____ ____ &nbsp;&nbsp; Expiry __ / __</div>
  <div class="abs form-text" style="left:17px;top:244px">Cardholder's Name: ...........................................................................................</div>
  <div class="abs form-text" style="left:17px;top:264px">Cardholder's Signature: ....................................................................................</div>
  <div class="abs form-text" style="left:17px;top:284px">Date: ...............................</div>

  <h3 class="abs form-head" style="left:17px;top:343px">SPONSORSHIP PACKAGE:</h3>
  <div class="abs form-text" style="left:13px;top:375px"><span class="box"></span>Gold ($5,000)<span style="margin-left:10px"></span><span class="box"></span>Silver ($2,500)<span style="margin-left:10px"></span><span class="box"></span>Bronze ($650)<span style="margin-left:10px"></span><span class="box"></span>Additional Players ($150)</div>
  <div class="abs field-row shade" style="top:403px">COMPANY:</div>
  <div class="abs field-row" style="top:420px">ADDRESS:</div>
  <div class="abs field-row shade" style="top:437px">SUBURB:</div>
  <div class="abs field-row" style="top:454px">P/CODE:</div>
  <div class="abs field-row shade" style="top:471px">MOBILE:</div>
  <div class="abs field-row" style="top:488px">CONTACT NAME:</div>
  <div class="abs field-row shade" style="top:505px">CONTACT EMAIL:</div>

  <h3 class="abs form-head" style="left:419px;top:49px">TEAM NAME:</h3>
  <div class="abs" style="left:419px;top:64px;width:345px;height:1px;background:var(--band)"></div>
  <div class="abs player" style="top:72px"><div class="bar">PLAYER 1</div><div class="cap">OFFICIAL GA H/CAP</div></div>
  <div class="abs player" style="top:118px"><div class="bar">PLAYER 2</div><div class="cap">OFFICIAL GA H/CAP</div></div>
  <div class="abs player" style="top:165px"><div class="bar">PLAYER 3</div><div class="cap">OFFICIAL GA H/CAP</div></div>
  <div class="abs player" style="top:211px"><div class="bar">PLAYER 4</div><div class="cap">OFFICIAL GA H/CAP</div></div>
  <div class="abs player" style="top:258px"><div class="bar">PLAYER 5</div><div class="cap">OFFICIAL GA H/CAP</div></div>
  <div class="abs player" style="top:304px"><div class="bar">PLAYER 6</div><div class="cap">OFFICIAL GA H/CAP</div></div>
  <div class="abs player" style="top:351px"><div class="bar">PLAYER 7</div><div class="cap">OFFICIAL GA H/CAP</div></div>
  <div class="abs player" style="top:397px"><div class="bar">PLAYER 8</div><div class="cap">OFFICIAL GA H/CAP</div></div>
  <p class="abs fine" style="left:419px;top:441px;width:355px">Please Note: Any player without an official GA H/Cap will be given a maximum handicap of 27(Males) &amp; 36 (Females).</p>
  <div class="abs" style="left:419px;top:463px;width:355px;height:1px;background:var(--band)"></div>
  <p class="abs fine" style="left:419px;top:474px;font-weight:700">CANCELLATION TERMS</p>
  <p class="abs fine" style="left:419px;top:486px;width:352px">If the organiser cancels the event prior to the scheduled date, the sponsor is entitled to a 100% refund. If the event is rescheduled by the organiser, and the player or sponsor can reasonably demonstrate their inability to participate they will be entitled to a full refund. In the event of a player or sponsor cancellation, the Lakeside Service Club reserves the right to retain monies paid in full unless resold. Any cancellations must be advised in writing via email to the Convenor Helena Whitford (helena.whitford@mailbox.com).</p>
  <svg class="abs" style="left:0;top:548px" width="792" height="12" viewBox="0 0 792 12" aria-hidden="true"><polygon points="200,0 606,0 620,12 186,12" fill="#34405b"/></svg>
</section>

</main>
</body>
</html>
```